refresh/modernization of affiliate website template

Make this website look better. The site is comprised of various sections (nav, hero, products, FAQ, testimonials, gallery, contact us, blog listing page, single post page) that are modular in nature and it would be great if the genera template of the site was reusable with industries other than travel. We left the "look and feel" sliders in the neutral position because we are not too sure what we want and thus would like to see various approaches.

3 page

```html
<!DOCTYPE html>
<html lang="en">
<head>
<meta charset="utf-8">
<title>Wander with Grace</title>
<link href="https://fonts.googleapis.com/css2?family=Montserrat:wght@600;700&family=Open+Sans:wght@400;700&display=swap" rel="stylesheet">
<style>
  :root {
    --ink: #0d0d0d;
    --body: #4a4a4a;
    --brand: #4b2b9b;
    --brand-mid: #8467c6;
    --brand-light: #d5c2f7;
    --photo-top: #7f9fbe;
    --photo-bottom: #d9a47e;
    --paper: #ffffff;
  }
  * { margin: 0; padding: 0; box-sizing: border-box; }
  html, body { width: 1200px; height: 675px; overflow: hidden; background: var(--paper); }
  .page { position: relative; width: 1200px; height: 675px; overflow: hidden; background: var(--paper); }
  .hero-visual { position: absolute; inset: 0; width: 1200px; height: 675px; }
  .brand {
    position: absolute; left: 62px; top: 46px;
    font-family: "Montserrat", sans-serif; font-weight: 700; color: var(--ink);
    font-size: 24px; line-height: 26px;
  }
  .brand span { display: block; }
  .nav-link {
    position: absolute; top: 70px;
    font-family: "Montserrat", sans-serif; font-weight: 600; font-size: 12px;
    color: var(--ink); text-decoration: none; white-space: nowrap;
  }
  .nav-cta {
    position: absolute; left: 1014px; top: 54px; width: 123px; height: 46px;
    background: var(--brand); color: var(--paper); border-radius: 2px;
    font-family: "Montserrat", sans-serif; font-weight: 700; font-size: 15px;
    display: flex; align-items: center; justify-content: center; text-decoration: none;
  }
  .hero-title {
    position: absolute; left: 61px; top: 246px;
    font-family: "Open Sans", sans-serif; font-weight: 400; font-size: 44px;
    line-height: 50px; color: var(--ink); white-space: nowrap;
  }
  .hero-title strong { display: block; font-weight: 700; color: var(--brand); }
  .hero-text {
    position: absolute; left: 62px; top: 359px; width: 380px;
    font-family: "Open Sans", sans-serif; font-size: 15px; line-height: 18.2px; color: var(--body);
  }
  .hero-cta {
    position: absolute; left: 62px; top: 465px; width: 169px; height: 47px;
    background: var(--brand); color: var(--paper); border-radius: 2px;
    font-family: "Montserrat", sans-serif; font-weight: 700; font-size: 15px;
    display: flex; align-items: center; justify-content: center; text-decoration: none;
  }
</style>
</head>
<body>
<div class="page">
  <svg class="hero-visual" viewBox="0 0 1200 675">
    <defs>
      <linearGradient id="photoFill" x1="0" y1="0" x2="0" y2="1">
        <stop offset="0" stop-color="var(--photo-top)"/>
        <stop offset="1" stop-color="var(--photo-bottom)"/>
      </linearGradient>
    </defs>
    <circle cx="1000" cy="375" r="484" fill="var(--brand-light)"/>
    <circle cx="1000" cy="375" r="465" fill="var(--brand-mid)"/>
    <circle cx="1000" cy="375" r="449" fill="url(#photoFill)" role="img" aria-label="Travel photo: aircraft wing seen from a cabin window above the clouds"/>
  </svg>

  <div class="brand"><span>Wander</span><span>with Grace</span></div>

  <nav>
    <a class="nav-link" href="#" style="left:386px">Features</a>
    <a class="nav-link" href="#" style="left:469px">Travel Tips and Answers</a>
    <a class="nav-link" href="#" style="left:694px">Products</a>
    <a class="nav-link" href="#" style="left:777px">FAQs</a>
    <a class="nav-link" href="#" style="left:839px">Testimonials</a>
    <a class="nav-link" href="#" style="left:943px">Gallery</a>
    <a class="nav-cta" href="#">Contact Us</a>
  </nav>

  <h1 class="hero-title">Unlock the world<strong>with style</strong></h1>
  <p class="hero-text">Your ultimate guide to traveling internationally and domestically. Discover exciting travel tips, answer your questions and find cool travel products to enhance your journey.</p>
  <a class="hero-cta" href="#">Start Exploring</a>
</div>
</body>
</html>
```